Quillstone Business Card

We need a business card design. We have a logo from a previous Sketchfold project and I am attaching the logo files in jpeg and photoshop.

```html
<!DOCTYPE html>
<html lang="en">
<head>
<meta charset="utf-8">
<title>Quillstone Business Card</title>
<link rel="stylesheet" href="https://fonts.googleapis.com/css2?family=Mulish:wght@600;700;800&display=swap">
<style>
  :root {
    --backdrop: #d9d9d9;
    --card-dark-top: #4a4a4a;
    --card-dark-bottom: #1f1f1f;
    --card-light: #ffffff;
    --ink: #3d3d3d;
    --ink-soft: #4a4a4a;
    --brand-green: #4caf50;
    --brand-green-deep: #3e9a42;
    --wave-grey: #5a5a5a;
    --wave-grey-deep: #3f3f3f;
    --logo-white: #f2f2f2;
  }
  * { box-sizing: border-box; margin: 0; padding: 0; }
  html, body {
    width: 1200px;
    height: 800px;
    overflow: hidden;
  }
  body {
    background: var(--backdrop);
    font-family: "Mulish", "Helvetica Neue", Arial, sans-serif;
    position: relative;
  }
  .card {
    position: absolute;
    top: 250px;
    width: 520px;
    height: 300px;
    border-radius: 4px;
    overflow: hidden;
    box-shadow: 0 10px 24px rgba(0, 0, 0, 0.18);
  }
  /* Front: dark side with the company name */
  .card--front {
    left: 50px;
    background: linear-gradient(160deg, var(--card-dark-top), var(--card-dark-bottom));
    display: flex;
    align-items: center;
    justify-content: center;
  }
  .brand-lockup {
    display: flex;
    align-items: center;
    gap: 14px;
  }
  .brand-lockup__square {
    width: 30px;
    height: 30px;
    background: var(--brand-green);
  }
  .brand-lockup__name {
    font-weight: 800;
    font-size: 54px;
    letter-spacing: -1px;
    color: var(--logo-white);
  }
  /* Back: contact side */
  .card--back {
    left: 630px;
    background: var(--card-light);
  }
  .card__wave {
    position: absolute;
    inset: 0;
    width: 100%;
    height: 100%;
  }
  .card__brand-mark {
    position: absolute;
    top: 52px;
    right: 34px;
    font-weight: 800;
    font-size: 34px;
    letter-spacing: -0.5px;
    color: var(--ink);
  }
  .contact {
    position: absolute;
    left: 34px;
    top: 44px;
    color: var(--ink-soft);
    font-weight: 700;
  }
  .contact__name {
    position: relative;
    font-size: 21px;
    font-weight: 800;
    color: var(--ink);
    padding-left: 18px;
    line-height: 1.1;
  }
  .contact__name::before {
    content: "";
    position: absolute;
    left: 0;
    top: 8px;
    width: 8px;
    height: 8px;
    background: var(--ink);
    transform: rotate(45deg);
  }
  .contact__position {
    font-size: 15px;
    font-weight: 800;
    color: var(--brand-green);
    padding-left: 18px;
    margin-bottom: 22px;
  }
  .contact__address {
    font-size: 14px;
    line-height: 1.35;
    padding-left: 18px;
    margin-bottom: 16px;
  }
  .contact__lines {
    list-style: none;
    font-size: 14px;
    line-height: 1.35;
    padding-left: 18px;
  }
  .contact__label {
    color: var(--brand-green);
    font-weight: 800;
  }
</style>
</head>
<body>
  <section class="card card--front" aria-label="Business card front">
    <div class="brand-lockup">
      <span class="brand-lockup__square"></span>
      <span class="brand-lockup__name">Quillstone</span>
    </div>
  </section>

  <section class="card card--back" aria-label="Business card back">
    <svg class="card__wave" viewBox="0 0 520 300" preserveAspectRatio="none" aria-hidden="true">
      <path d="M0,268 C170,250 340,205 520,112 L520,300 L0,300 Z" fill="var(--wave-grey)"/>
      <path d="M0,278 C170,262 340,222 520,150 L520,300 L0,300 Z" fill="var(--brand-green)"/>
      <path d="M0,288 C170,276 340,242 520,172 L520,300 L0,300 Z" fill="var(--wave-grey-deep)"/>
    </svg>

    <div class="card__brand-mark">Quillstone</div>

    <div class="contact">
      <p class="contact__name">YOUR NAME</p>
      <p class="contact__position">Company Position</p>
      <p class="contact__address">111 Your Street Address<br>206 Town, CT 00000</p>
      <ul class="contact__lines">
        <li><span class="contact__label">E:</span> youremail@domain.com</li>
        <li><span class="contact__label">P:</span> 111-222-444</li>
        <li><span class="contact__label">F:</span> 111-222-333</li>
      </ul>
    </div>
  </section>
</body>
</html>
```